certificate to present to patients after successful vasectomy

creation of a A4 sized colour certificate that can be presented to patients after their three month semen test confirms a successful vasectomy.
I have attached my current logo for Clearway Snip Clinic with the colours blue and green. I have attached a collage of example fun images related to congratulating men after their vasectomy.

Target Market(s)

A fun certificate to provide to men after a successful vasectomy. THis is a bit more playful/fun than traditional medical illustration/medical information. Men can stick it on the fridge or wave it about a family events to mortify their children.

Font styles to use
Sans Serif

Colors

Designer to choose colors to be used in the design.

Requirements
Must have
• Clearway Snip Clinic Logo and these or complimentary colours
• Be editable to add the patients name and date of certificate
Nice to have
• continuation of design themes from logo
Should not have
• should not have realistic or medical illustration of penis/scrotum. This should be a fun/silly certificate they can put on the family fridge or cork board

```html
<!DOCTYPE html>
<html lang="en">
<head>
<meta charset="utf-8">
<title>Vasectomy Success Certificate – Clearway Snip Clinic</title>
<link rel="stylesheet" href="https://fonts.googleapis.com/css2?family=Raleway:wght@300;700&family=Kaushan+Script&family=Tinos&family=Allura&display=swap">
<style>
  :root {
    --page: #ffffff;
    --card: #ececec;
    --brand-blue: #2a88c8;
    --brand-green: #8cc63f;
    --name-blue: #1f7fcb;
    --ink: #3a3a3a;
    --ink-dark: #1a1a1a;
    --emblem-bg: #e6e6e6;
    --emblem-tone: #cfcfcf;
  }
  * { box-sizing: border-box; margin: 0; padding: 0; }
  html, body { width: 1200px; height: 858px; overflow: hidden; background: var(--page); }
  .certificate {
    position: relative;
    width: 1200px;
    height: 858px;
    background: var(--page);
  }
  .certificate__card {
    position: absolute;
    left: 17px; top: 17px;
    width: 1166px; height: 823px;
    background: var(--card);
  }
  .certificate__frame { position: absolute; left: 0; top: 0; }
  .certificate__heading {
    position: absolute;
    top: 128px; left: 0; width: 100%;
    text-align: center;
    font-family: "Raleway", sans-serif;
    font-weight: 300;
    font-size: 47px;
    letter-spacing: 2px;
    color: var(--ink);
    line-height: 1;
  }
  .certificate__emblem {
    position: absolute;
    left: 530px; top: 190px;
    width: 118px; height: 108px;
    background: var(--emblem-bg);
    display: flex; align-items: center; justify-content: center;
  }
  .certificate__emblem-shape {
    width: 62px; height: 92px;
    border-radius: 30px 30px 8px 8px;
    background: linear-gradient(180deg, var(--emblem-tone), var(--emblem-bg));
  }
  .certificate__patient {
    position: absolute;
    top: 358px; left: 0; width: 100%;
    text-align: center;
    font-family: "Kaushan Script", cursive;
    font-size: 92px;
    color: var(--name-blue);
    line-height: 1.2;
  }
  .certificate__statement {
    position: absolute;
    top: 528px; left: 0; width: 100%;
    text-align: center;
    font-family: "Tinos", serif;
    font-size: 31px;
    letter-spacing: 1px;
    color: var(--ink);
    line-height: 1;
  }
  .certificate__signature {
    position: absolute;
    top: 616px; left: 386px; width: 400px;
    text-align: center;
    font-family: "Allura", cursive;
    font-size: 52px;
    color: var(--ink-dark);
    line-height: 1;
  }
  .certificate__signatory {
    position: absolute;
    top: 688px; left: 386px; width: 400px;
    text-align: center;
    font-family: "Tinos", serif;
    font-size: 17px;
    color: var(--ink);
  }
  .certificate__clinic {
    position: absolute;
    top: 720px; left: 386px; width: 400px;
    text-align: center;
    font-family: "Raleway", sans-serif;
    font-weight: 700;
    font-size: 17px;
    color: var(--brand-blue);
  }
  .clinic-mark {
    position: absolute;
    left: 64px; top: 714px;
    font-family: "Raleway", sans-serif;
    font-weight: 700;
    font-size: 25px;
    line-height: 26px;
    letter-spacing: 0.5px;
    color: var(--brand-blue);
    text-transform: uppercase;
  }
</style>
</head>
<body>
<main class="certificate">
  <div class="certificate__card"></div>

  <svg class="certificate__frame" width="1200" height="858" viewBox="0 0 1200 858" aria-hidden="true">
    <g fill="none" stroke-width="3.5" stroke-linecap="square">
      <path class="frame-outer" stroke="var(--brand-blue)" d="M52 675 V52 H1150 V806 H258"/>
      <path class="frame-inner" stroke="var(--brand-green)" d="M78 642 V77 H1122 V780 H272"/>
    </g>
  </svg>

  <h1 class="certificate__heading">CONGRATULATIONS!</h1>

  <div class="certificate__emblem" role="img" aria-label="Line-drawn rose emblem in a goblet">
    <div class="certificate__emblem-shape"></div>
  </div>

  <p class="certificate__patient">John Doe</p>
  <p class="certificate__statement">HAD A SUCCESSFUL VASECTOMY!</p>

  <p class="certificate__signature">Martin Hale</p>
  <p class="certificate__signatory">Dr Martin Hale</p>
  <p class="certificate__clinic">CLEARWAY SNIP CLINIC</p>

  <div class="clinic-mark">Clearway<br>Snip<br>Clinic</div>
</main>
</body>
</html>
```